business card, stationary, email signature, envelopes
Bold Grins, PLLC
business card, stationary, email signature, envelopes - Medical
Creative Brief
Bright & Fun-filled
714 Harwick Ave Dover, NH 03827
boldgrinspllc@quorvamail.com
BoldGrinsPLLC.com

```html
<!DOCTYPE html>
<html lang="en">
<head>
<meta charset="utf-8">
<title>Bold Grins, PLLC – Business Card</title>
<link href="https://fonts.googleapis.com/css2?family=Nunito:wght@400;600;800&display=swap" rel="stylesheet">
<style>
  :root {
    --bg: #e4e5e7;
    --card: #ffffff;
    --sky: #1d8bd3;
    --navy: #2d4b7e;
    --pink: #e0256f;
    --ink: #3a3f47;
    --muted: #6a707a;
  }
  * { margin: 0; padding: 0; box-sizing: border-box; }
  html, body { width: 1200px; height: 895px; overflow: hidden; }
  body {
    background: var(--bg);
    font-family: "Nunito", Arial, sans-serif;
    position: relative;
  }
  .card {
    position: absolute;
    width: 520px;
    height: 297px;
    background: var(--card);
    box-shadow: 0 6px 18px rgba(0,0,0,0.12);
    overflow: hidden;
  }
  .card--front { left: 50px; top: 299px; }
  .card--back { left: 630px; top: 299px; }

  .brand {
    position: absolute;
    display: flex;
    align-items: center;
    gap: 8px;
    color: var(--navy);
    font-weight: 800;
    letter-spacing: -0.5px;
  }
  .brand__dot {
    border-radius: 50%;
    background: var(--pink);
  }
  .card--front .brand { left: 22px; top: 22px; font-size: 34px; }
  .card--front .brand__dot { width: 12px; height: 12px; }
  .card--back .brand { left: 50%; top: 50%; transform: translate(-50%, -50%); font-size: 44px; }
  .card--back .brand__dot { width: 15px; height: 15px; }

  .accent-block {
    position: absolute;
    left: 0; top: 104px;
    width: 186px; height: 38px;
    background: var(--sky);
  }
  .web-band {
    position: absolute;
    left: 193px; right: 0;
    top: 128px; height: 58px;
    background: var(--navy);
    color: #fff;
    font-size: 13px;
    font-weight: 600;
    letter-spacing: 0.6px;
    display: flex;
    align-items: center;
    padding-left: 22px;
  }
  .person {
    position: absolute;
    right: 26px; top: 84px;
    text-align: right;
    color: var(--ink);
  }
  .person__name { font-size: 15px; font-weight: 800; letter-spacing: 1px; }
  .person__role { font-size: 11px; font-weight: 600; letter-spacing: 1px; color: var(--muted); }

  .contact-list {
    position: absolute;
    list-style: none;
    font-size: 9.5px;
    color: var(--ink);
  }
  .contact-list li { display: flex; align-items: center; gap: 7px; height: 17px; }
  .contact-list svg { width: 11px; height: 11px; flex: none; }
  .contact-list--info { left: 22px; top: 152px; }
  .contact-list--social { left: 212px; top: 222px; }
</style>
</head>
<body>
  <section class="card card--front" aria-label="Business card front">
    <div class="brand"><span class="brand__name">Bold Grins</span><span class="brand__dot"></span></div>
    <div class="accent-block"></div>
    <div class="person">
      <p class="person__name">DANA WHITLOCK</p>
      <p class="person__role">MANAGER</p>
    </div>
    <div class="web-band">BoldGrinsPLLC.com</div>
    <ul class="contact-list contact-list--info">
      <li>
        <svg viewBox="0 0 12 12"><rect width="12" height="12" rx="2" fill="#3a3f47"/><path d="M6 2.5a2.3 2.3 0 0 0-2.3 2.3C3.7 6.6 6 9.5 6 9.5s2.3-2.9 2.3-4.7A2.3 2.3 0 0 0 6 2.5z" fill="#fff"/></svg>
        714 Harwick Ave Dover, NH 03827
      </li>
      <li>
        <svg viewBox="0 0 12 12"><rect width="12" height="12" rx="2" fill="#3a3f47"/><path d="M3.5 2.8l1.4-.3.8 1.8-.9.7a5 5 0 0 0 2.2 2.2l.7-.9 1.8.8-.3 1.4C6.4 8.6 3.4 5.6 3.5 2.8z" fill="#fff"/></svg>
        603 555 0142
      </li>
      <li>
        <svg viewBox="0 0 12 12"><rect width="12" height="12" rx="2" fill="#3a3f47"/><rect x="2.5" y="3.5" width="7" height="5" fill="none" stroke="#fff" stroke-width="1"/><path d="M2.5 3.5L6 6.3l3.5-2.8" fill="none" stroke="#fff" stroke-width="1"/></svg>
        boldgrinspllc@quorvamail.com
      </li>
    </ul>
    <ul class="contact-list contact-list--social">
      <li>
        <svg viewBox="0 0 12 12"><circle cx="6" cy="6" r="6" fill="#3a3f47"/><circle cx="6" cy="6" r="3" fill="none" stroke="#fff" stroke-width="1"/></svg>
        BoldGrinsPLLC.com
      </li>
      <li>
        <svg viewBox="0 0 12 12"><circle cx="6" cy="6" r="6" fill="#3a3f47"/></svg>
        @boldgrinsdental
      </li>
      <li>
        <svg viewBox="0 0 12 12"><circle cx="6" cy="6" r="6" fill="#3a3f47"/></svg>
        /boldgrinsnh
      </li>
    </ul>
  </section>

  <section class="card card--back" aria-label="Business card back">
    <div class="brand"><span class="brand__name">Bold Grins</span><span class="brand__dot"></span></div>
  </section>
</body>
</html>
```